Spiritual Healing bussiness needs logo/business card

Simple, clean looking logo/card
For spiritual business with healing services and occult rituals

Contact Information for Business Card

Needs my name: Tovin Harlowe
Business name: Velka Healing Shop
Services provided and worded in this way:

Reiki Healing
Tarot
Oils
Rituals Of Change

Can look occult like but with light energy.

Colors
0255a3
3276b5
85abd2
33a6d7
85cae6
0292cd

```html
<!DOCTYPE html>
<html lang="en">
<head>
<meta charset="utf-8">
<title>Velka Healing Shop – Business Card</title>
<link href="https://fonts.googleapis.com/css2?family=Cinzel:wght@400&family=Open+Sans:wght@400&display=swap" rel="stylesheet">
<style>
  :root {
    --deep-blue: #0255a3;
    --mid-blue: #3276b5;
    --soft-blue: #85abd2;
    --sky-blue: #33a6d7;
    --pale-sky: #85cae6;
    --bright-blue: #0292cd;
    --paper: #f4f4f3;
    --ink: #1a1a1a;
    --stage: #5a5a5a;
  }
  * { margin: 0; padding: 0; box-sizing: border-box; }
  html, body { width: 1200px; height: 900px; overflow: hidden; }
  body {
    background: var(--stage);
    display: flex;
    flex-direction: column;
    align-items: center;
    justify-content: center;
    gap: 44px;
  }
  .card {
    width: 600px;
    height: 343px;
    border-radius: 26px;
    position: relative;
    overflow: hidden;
  }
  .card--front {
    background: linear-gradient(160deg, var(--sky-blue) 0%, var(--bright-blue) 55%, var(--deep-blue) 100%);
    color: #fff;
  }
  .card--back {
    background: var(--paper);
    color: var(--ink);
  }

  /* Brand lock-up: name stacked in two lines, single colour and weight */
  .brand {
    position: absolute;
    display: flex;
    align-items: center;
    gap: 14px;
  }
  .brand__mark {
    width: 18px;
    height: 18px;
    border-radius: 50%;
    flex: none;
  }
  .brand__name {
    font-family: 'Cinzel', serif;
    font-weight: 400;
    display: flex;
    flex-direction: column;
    align-items: center;
    line-height: 1;
  }
  .brand__word {
    font-size: 40px;
    letter-spacing: 0.06em;
  }
  .brand__tagline {
    font-size: 11px;
    letter-spacing: 0.42em;
    margin-top: 6px;
    padding-left: 0.42em;
    white-space: nowrap;
  }

  .card--front .brand {
    left: 50%;
    top: 118px;
    transform: translateX(-50%);
  }
  .card--front .brand__mark { border: 1.5px solid #fff; }
  .card--front .brand__name { color: #fff; }

  .services {
    position: absolute;
    left: 0;
    right: 0;
    bottom: 62px;
    font-family: 'Cinzel', serif;
    font-size: 15px;
    letter-spacing: 0.06em;
    display: flex;
    justify-content: center;
    gap: 14px;
    white-space: nowrap;
  }
  .services__divider { opacity: 0.9; }

  .card--back .brand {
    left: 56px;
    top: 186px;
  }
  .card--back .brand__mark { border: 1.5px solid var(--deep-blue); }
  .card--back .brand__name { color: var(--deep-blue); }
  .card--back .brand__word { font-size: 36px; }
  .card--back .brand__tagline { font-size: 10px; }

  .contact {
    position: absolute;
    left: 352px;
    top: 96px;
  }
  .contact__name {
    font-family: 'Cinzel', serif;
    font-size: 22px;
    letter-spacing: 0.05em;
    margin-bottom: 14px;
    white-space: nowrap;
  }
  .contact__line {
    display: flex;
    align-items: center;
    gap: 9px;
    font-family: 'Open Sans', sans-serif;
    font-size: 13px;
    margin-bottom: 8px;
    white-space: nowrap;
  }
  .contact__icon { width: 13px; height: 13px; fill: var(--deep-blue); flex: none; }
</style>
</head>
<body>
  <section class="card card--front">
    <div class="brand">
      <span class="brand__mark"></span>
      <span class="brand__name">
        <span class="brand__word">VELKA</span>
        <span class="brand__tagline">HEALING SHOP</span>
      </span>
    </div>
    <div class="services">
      <span>Reiki Healing</span><span class="services__divider">I</span>
      <span>Tarot</span><span class="services__divider">I</span>
      <span>Oils</span><span class="services__divider">I</span>
      <span>Rituals Of Change</span>
    </div>
  </section>

  <section class="card card--back">
    <div class="brand">
      <span class="brand__mark"></span>
      <span class="brand__name">
        <span class="brand__word">VELKA</span>
        <span class="brand__tagline">HEALING SHOP</span>
      </span>
    </div>
    <div class="contact">
      <p class="contact__name">Tovin Harlowe</p>
      <p class="contact__line">
        <svg class="contact__icon" viewBox="0 0 16 16" aria-hidden="true"><path d="M1 5c0-2 3-3 7-3s7 1 7 3v1.5h-3.5V5H4.5v1.5H1z M3 8l2-2h6l2 2v6H3z"/></svg>
        <span>000 000 0000</span>
      </p>
      <p class="contact__line">
        <svg class="contact__icon" viewBox="0 0 16 16" aria-hidden="true"><path d="M1 3h14v10H1z" fill="none" stroke="#0255a3" stroke-width="1.6"/><path d="M1 3l7 6 7-6" fill="none" stroke="#0255a3" stroke-width="1.6"/></svg>
        <span>youremail@xyz.com</span>
      </p>
    </div>
  </section>
</body>
</html>
```